Book and Ebook Cover for my Upcoming Book

About the Book
------------------
I need a book, ebook and if possible audio cover design for my upcoming book - Lanterns & Larkspur. This is my first book and really looking for a great book cover. The book is about my story, living with Mental Health and how to reclaim control of your life.

Quillbarrow
-----------
I am using quillbarrow.com to self-publish my book so in case of any design-related questions you can just search info on their website.

I have an initial theme I am thinking for the design book cover which I have attached. You can use this as a starting point.

Idea for the theme
---------------------
I am thinking about a phoenix to represent rising from the ashes and rebirth. The phoenix motif will be continued throughout the interior pages of the book. I'd like the cover of the book to be minimal, white with gold lettering, and maybe incorporating wings? feel free to play around with the idea and up for suggestions.

If you can think of something along these lines and make it a lot better that would be great.

What I need
---------------
The book is complete and is Trim size is 6.14 x 9.21” (234 x 156mm). I would need-
1. Book Cover
2. Back & Spine Design
3. Source File
4. Ebook Cover
5. Need multiple revisions to get the best possible outcome
6. My name and book title should also on the front cover
7. The book title should be bigger size than the subtitle

If you can give me Audiobook cover, I would love that as well and can pay extra for it if needed.

I love this for the interior phoenix motif:
https://craftbazaarly.com/InkMoth/7720458-Watercolor-Heron-Clipart-Set#fullscreen

The only other actual book cover I found online that remotely relates to what I am looking for is this -
https://www.lookfinder.example/url?sa=i&url=https%3A%2F%2Fpixelmoor.com%2Fvantrell&psig=QxTrPLm3KZ9vBwE2dYcN41HoJuSA&ust=1598415525610000&source=images&cd=vfe&ved=0CAIQjRxqFwoTCPD_toPAtesCFQAAAAAdAAAAABAD

Target Market(s)

Personal Development
Mental health

Requirements
Must have
• 1. Book Cover
2. Back & Spine Design
3. Source File
4. Ebook Cover
Nice to have
• Audiobook cover as I eventually will be releasing the audio version of the book

```html
<!DOCTYPE html>
<html lang="en">
<head>
<meta charset="UTF-8">
<title>Lanterns &amp; Larkspur — Book Cover</title>
<link rel="stylesheet" href="https://fonts.googleapis.com/css2?family=Cormorant+Garamond:wght@600&family=Crimson+Text&display=swap">
<style>
  :root {
    --paper: #f8f8f6;
    --gold: #d9a93f;
    --gold-deep: #c8942b;
    --ink: #111111;
    --flame-yellow: #fbd45c;
    --flame-orange: #f0a040;
    --flame-red: #e0533a;
  }
  html, body {
    margin: 0;
    padding: 0;
    overflow: hidden;
    background: var(--paper);
  }
  .cover {
    position: relative;
    width: 840px;
    height: 1200px;
    background: var(--paper);
    overflow: hidden;
  }
  .title {
    position: absolute;
    left: 0;
    top: 76px;
    width: 840px;
    margin: 0;
    text-align: center;
    font-family: "Cormorant Garamond", Georgia, serif;
    font-weight: 600;
    color: var(--gold);
    text-shadow: 0 1px 0 var(--gold-deep);
    line-height: 1;
  }
  .title-line {
    display: block;
    font-size: 84px;
    letter-spacing: 2px;
  }
  .title-amp {
    display: block;
    font-size: 66px;
    margin: 14px 0 12px;
  }
  .subtitle {
    position: absolute;
    left: 0;
    top: 360px;
    width: 840px;
    margin: 0;
    text-align: center;
    font-family: "Crimson Text", Georgia, serif;
    font-size: 25px;
    line-height: 28px;
    color: var(--ink);
  }
  .phoenix-art {
    position: absolute;
    left: 250px;
    top: 450px;
    width: 340px;
    height: 565px;
    border-radius: 46% 46% 40% 40%;
    background: radial-gradient(ellipse at 50% 45%,
      var(--flame-yellow) 0%,
      var(--flame-orange) 45%,
      rgba(224, 83, 58, 0.55) 70%,
      rgba(248, 248, 246, 0) 100%);
  }
  .author {
    position: absolute;
    left: 0;
    top: 1090px;
    width: 840px;
    margin: 0;
    text-align: center;
    font-family: "Cormorant Garamond", Georgia, serif;
    font-weight: 600;
    font-size: 58px;
    letter-spacing: 1px;
    color: var(--ink);
  }
</style>
</head>
<body>
  <main class="cover">
    <h1 class="title">
      <span class="title-line">LANTERNS</span>
      <span class="title-amp">&amp;</span>
      <span class="title-line">LARKSPUR</span>
    </h1>
    <p class="subtitle">Living with Mental Health and how to<br>reclaim control of your life</p>
    <div class="phoenix-art" role="img" aria-label="Watercolour phoenix rising with wings raised, in yellow, orange and red flame tones"></div>
    <p class="author">MEERAN VS</p>
  </main>
</body>
</html>
```